Personal Trainer Business Card

I need a business card using a logo I already have.
The logo is in uploaded files.
Card is to give to prospective clients that interested in health and beauty or already exercise. Would like logo on front or other abstract images and details on back.
Like modern design that also unique and eye catching rather than just generic fitness gym/fitness theme.

Target Market(s)

Main clients are trendy women aged 25-60.

Industry/Entity Type

Fitness

Contact Information for Business Card

Email: tom@tomharvecoaching.com

web: www.tomharvecoaching.com

mobile: 0493 257618

facebook: www.facebook.com/tomharvecoaching

Location is: Coral Heights

Font styles to use
Sans Serif

Colors
000000
1b1b1b
333333

Requirements
Must have
• Logo on front
• black background of sorts on front (fine if mixed with dark grey or abstract)
• White background on back.
Nice to have
• I would like the front side with the logo appearing on it with black background. Fine with alternative ideas and layout.
• Would like the front to be modern, professional and cool/interesting.
• Fine with abstract or modern design.
• Reverse of the card some white background with details on it
• (I like simple fonts).
• CAn use same font colour as in logo in places or what whatever
Should not have
• Avoiding use of cheap pics such as weights

```html
<!DOCTYPE html>
<html lang="en">
<head>
<meta charset="utf-8">
<title>Tom Harve Coaching – Business Card</title>
<link rel="stylesheet" href="https://fonts.googleapis.com/css2?family=Roboto+Condensed:wght@300;700&display=swap">
<style>
  :root {
    --backdrop: #b59d6a;
    --card-black: #050708;
    --card-white: #f6f6f6;
    --gold: #ad8d54;
    --ink: #2a2a2a;
    --divider: #e2e2e2;
  }
  * { box-sizing: border-box; margin: 0; padding: 0; }
  html, body {
    width: 1200px; height: 1200px; overflow: hidden;
    background: var(--backdrop);
    font-family: "Roboto Condensed", "Arial Narrow", sans-serif;
  }
  .sheet {
    width: 1200px; height: 1200px;
    display: flex; flex-direction: column;
    align-items: center; justify-content: center; gap: 48px;
  }
  .card {
    width: 840px; height: 513px;
    border-radius: 6px;
    box-shadow: 0 10px 30px rgba(60, 40, 10, 0.25);
    position: relative;
    overflow: hidden;
  }
  .card--front {
    background: var(--card-black);
    display: flex; align-items: center; justify-content: center;
  }
  .brand {
    display: flex; align-items: center; gap: 20px;
    color: var(--gold);
    font-weight: 700;
    text-transform: uppercase;
    line-height: 1;
    white-space: nowrap;
  }
  .brand__mark {
    width: 22px; height: 22px; background: var(--gold); flex: none;
  }
  .brand__name { font-size: 60px; letter-spacing: 2px; }
  .card--back {
    background: var(--card-white);
    display: grid; grid-template-columns: 420px 420px;
  }
  .card--back .brand { gap: 14px; }
  .card--back .brand__name { font-size: 32px; letter-spacing: 1px; }
  .card--back .brand__mark { width: 14px; height: 14px; }
  .card__brand-side {
    display: flex; align-items: center; justify-content: center;
    border-right: 1px solid var(--divider);
    margin: 70px 0;
  }
  .contact {
    list-style: none;
    display: flex; flex-direction: column; justify-content: center; gap: 14px;
    padding-left: 44px;
    color: var(--ink);
    font-weight: 300;
    font-size: 27px;
    white-space: nowrap;
  }
  .contact__item { display: flex; align-items: center; gap: 14px; }
  .contact__icon { width: 22px; height: 22px; flex: none; fill: var(--gold); }
  .contact__icon--line { fill: none; stroke: var(--gold); stroke-width: 2; }
</style>
</head>
<body>
<main class="sheet">
  <section class="card card--front" aria-label="Card front">
    <div class="brand">
      <span class="brand__mark"></span>
      <span class="brand__name">Tom Harve Coaching</span>
    </div>
  </section>

  <section class="card card--back" aria-label="Card back">
    <div class="card__brand-side">
      <div class="brand">
        <span class="brand__mark"></span>
        <span class="brand__name">Tom Harve Coaching</span>
      </div>
    </div>
    <ul class="contact">
      <li class="contact__item">
        <svg class="contact__icon contact__icon--line" viewBox="0 0 24 24" aria-hidden="true"><path d="M2 5h20v14H2z"/><path d="M2 5l10 8 10-8"/></svg>
        tom@tomharvecoaching.com
      </li>
      <li class="contact__item">
        <svg class="contact__icon contact__icon--line" viewBox="0 0 24 24" aria-hidden="true"><circle cx="12" cy="12" r="10"/><path d="M2 12h20M12 2c3 3 3 17 0 20M12 2c-3 3-3 17 0 20"/></svg>
        www.tomharvecoaching.com
      </li>
      <li class="contact__item">
        <svg class="contact__icon" viewBox="0 0 24 24" aria-hidden="true"><path d="M6.6 10.8a15 15 0 0 0 6.6 6.6l2.2-2.2a1 1 0 0 1 1-.25 11.4 11.4 0 0 0 3.6.57 1 1 0 0 1 1 1V20a1 1 0 0 1-1 1A17 17 0 0 1 3 4a1 1 0 0 1 1-1h3.5a1 1 0 0 1 1 1c0 1.25.2 2.45.57 3.6a1 1 0 0 1-.25 1z"/></svg>
        0493 257618
      </li>
      <li class="contact__item">
        <svg class="contact__icon" viewBox="0 0 24 24" aria-hidden="true"><rect x="3" y="3" width="18" height="18" rx="2"/></svg>
        /tomharvecoaching
      </li>
      <li class="contact__item">
        <svg class="contact__icon" viewBox="0 0 24 24" aria-hidden="true"><path d="M12 2a7 7 0 0 0-7 7c0 5.2 7 13 7 13s7-7.8 7-13a7 7 0 0 0-7-7zm0 9.5A2.5 2.5 0 1 1 12 6.5a2.5 2.5 0 0 1 0 5z"/></svg>
        Coral Heights
      </li>
    </ul>
  </section>
</main>
</body>
</html>
```